Hal's Remedies Business Card Design Project

I need a business card designed for my pharmacy Hal's Remedies. I would like just the logo on one side, maybe with black background and white lettering. The other side I would also like to include my logo which is attached. Also, please include my name and the following information:
Hal Norwick Owner/Pharm D.
Business address is 7163 N Birch Rd Alder Falls, ND 57291.
Phone number is 555-318-6027 and fax # is 555-318-6031.
my email address is hal@halsremedies.example.
My website is www.halsremedies.example.
My business hours are Monday-Friday 9am-6 pm. Saturday 9am-1 pm. Sunday Closed.
I would like the design to include my logo colors, black, white, and neon green. Silver may be added as a highlight. Thanks.
Pharmacy
See above in product description

```html
<!DOCTYPE html>
<html lang="en">
<head>
<meta charset="utf-8">
<title>Hal's Remedies – Business Card</title>
<link rel="stylesheet" href="https://fonts.googleapis.com/css2?family=Open+Sans:wght@400;600;700&display=swap">
<style>
  :root {
    --ink: #231f20;
    --paper: #ffffff;
    --neon: #8dc63f;
    --backdrop: #b9b9bb;
  }
  * { box-sizing: border-box; margin: 0; padding: 0; }
  html, body { width: 1200px; height: 900px; overflow: hidden; }
  body {
    background: var(--backdrop);
    font-family: "Open Sans", Arial, sans-serif;
    display: flex;
    flex-direction: column;
    align-items: center;
    justify-content: center;
    gap: 36px;
  }
  .card {
    width: 700px;
    height: 400px;
    position: relative;
    overflow: hidden;
    background: var(--paper);
    box-shadow: 0 6px 18px rgba(0,0,0,.25);
  }

  /* Front */
  .front__head {
    position: absolute; left: 0; top: 0; width: 100%; height: 118px;
    display: flex; align-items: center; padding-left: 200px; gap: 18px;
  }
  .brand-dot { width: 26px; height: 26px; border-radius: 50%; background: var(--neon); flex: none; }
  .brand-divider { width: 2px; height: 62px; background: var(--ink); }
  .brand-name { font-weight: 700; font-size: 34px; color: var(--ink); letter-spacing: -1px; white-space: nowrap; }
  .front__rule { position: absolute; left: 0; top: 118px; width: 100%; height: 6px; background: var(--neon); }
  .front__body {
    position: absolute; left: 0; top: 124px; width: 100%; height: 226px;
    background: var(--ink); color: var(--paper);
  }
  .contact { position: absolute; left: 34px; top: 26px; list-style: none; font-size: 15px; line-height: 27px; }
  .contact li { display: flex; align-items: center; gap: 12px; }
  .contact svg { width: 14px; height: 14px; fill: var(--paper); flex: none; }
  .person { position: absolute; right: 40px; top: 118px; text-align: right; }
  .person__name { font-weight: 700; font-size: 30px; letter-spacing: 2px; line-height: 1.2; }
  .person__role { font-size: 17px; letter-spacing: 1.5px; margin-top: 2px; }
  .front__foot {
    position: absolute; left: 0; bottom: 0; width: 100%; height: 50px;
    display: flex; align-items: center; justify-content: space-between;
    padding: 0 34px; font-size: 14px; font-weight: 600; color: var(--ink);
  }
  .front__foot span { display: flex; align-items: center; gap: 8px; }
  .front__foot svg { width: 15px; height: 15px; flex: none; }

  /* Back */
  .back__brand {
    position: absolute; left: 30px; top: 0; width: 360px; height: 100%;
    display: flex; flex-direction: column; align-items: center; justify-content: center; gap: 22px;
  }
  .back__brand .brand-row { display: flex; align-items: center; gap: 14px; }
  .back__brand .brand-name { font-size: 36px; }
  .back__web { font-size: 13px; font-weight: 600; color: var(--ink); display: flex; align-items: center; gap: 6px; }
  .back__web svg { width: 13px; height: 13px; flex: none; }
  .back__divider { position: absolute; left: 410px; top: 85px; width: 2px; height: 230px; background: var(--ink); }
  .hours { position: absolute; left: 448px; top: 160px; list-style: none; font-size: 16px; font-weight: 700; color: var(--ink); line-height: 30px; }
  .hours li { display: flex; align-items: center; gap: 12px; white-space: nowrap; }
  .hours li::before { content: ""; width: 14px; height: 14px; border-radius: 50%; background: var(--neon); flex: none; }
</style>
</head>
<body>

<section class="card card--front" aria-label="Card front">
  <header class="front__head">
    <span class="brand-dot"></span>
    <span class="brand-divider"></span>
    <span class="brand-name">Hal's Remedies</span>
  </header>
  <div class="front__rule"></div>
  <div class="front__body">
    <ul class="contact">
      <li><svg viewBox="0 0 24 24"><path d="M12 2a7 7 0 0 0-7 7c0 5 7 13 7 13s7-8 7-13a7 7 0 0 0-7-7zm0 9.5A2.5 2.5 0 1 1 12 6.5a2.5 2.5 0 0 1 0 5z"/></svg>7163 N Birch Rd, Alder Falls, ND 57291</li>
      <li><svg viewBox="0 0 24 24"><path d="M6.6 10.8a15 15 0 0 0 6.6 6.6l2.2-2.2a1 1 0 0 1 1-.25 11.4 11.4 0 0 0 3.6.57 1 1 0 0 1 1 1V20a1 1 0 0 1-1 1A17 17 0 0 1 3 4a1 1 0 0 1 1-1h3.5a1 1 0 0 1 1 1c0 1.25.2 2.45.57 3.57a1 1 0 0 1-.25 1z"/></svg>555-318-6027</li>
      <li><svg viewBox="0 0 24 24"><path d="M6 2h9l3 3v5H6zM3 11h18v9H3zm3 3v2h4v-2zm10-1a1 1 0 1 0 0 2 1 1 0 0 0 0-2z"/></svg>555-318-6031</li>
    </ul>
    <div class="person">
      <div class="person__name">Hal Norwick</div>
      <div class="person__role">Owner/Pharm D.</div>
    </div>
  </div>
  <footer class="front__foot">
    <span><svg viewBox="0 0 24 24" fill="var(--ink)"><path d="M2 5h20v14H2zm2 2v.5l8 5.5 8-5.5V7z"/></svg>hal@halsremedies.example</span>
    <span><svg viewBox="0 0 24 24" fill="none" stroke="var(--ink)" stroke-width="2"><circle cx="12" cy="12" r="9"/><path d="M3 12h18M12 3c3 3 3 15 0 18M12 3c-3 3-3 15 0 18"/></svg>www.halsremedies.example</span>
  </footer>
</section>

<section class="card card--back" aria-label="Card back">
  <div class="back__brand">
    <div class="brand-row">
      <span class="brand-dot"></span>
      <span class="brand-name">Hal's Remedies</span>
    </div>
    <div class="back__web"><svg viewBox="0 0 24 24" fill="none" stroke="var(--ink)" stroke-width="2"><circle cx="12" cy="12" r="9"/><path d="M3 12h18M12 3c3 3 3 15 0 18M12 3c-3 3-3 15 0 18"/></svg>www.halsremedies.example</div>
  </div>
  <div class="back__divider"></div>
  <ul class="hours">
    <li>Monday-Friday 9am-6 pm</li>
    <li>Saturday 9am-1 pm</li>
    <li>Sunday Closed</li>
  </ul>
</section>

</body>
</html>
```